IT Company Business Card Design w/Stationary Design

We have a great logo we like! We are looking to redesign our business cards and all company logo'd merchandise/materials.

We are an IT Company located near the Bay Area (San Francisco, CA). We specialize in Managed Services and offer complete IT Computer and Network Support to Businesses of all sizes. We thrive on making a lasting impression. We have been doing IT for 15yrs+ but are young at heart. We like to stand out and be different. We want to be unique and have a recognizable brand. We need our logo to represent who we are. We are young, professional, creative and outstanding. We don't want to blend in, we want to stand out. Our business card needs to stand out and grab attention. Something Bold, yet simple and clean. (I will provide ideas of what we like to give a taste of what we are looking for).

The design can include any kind of texture/artistic design or sizing EXCEPT please "no square card designs" as they don't seem to fit in wallets very well. We dont mind curved edges, rounded corners, vertical layouts or horizontal layouts, embossing, letter press or raised surfaces. Again, we dont want to look average or plain or boring. :) Be creative - yet practical! We have ordered from ZEPL designs before and been very happy. Their card sizes tend to be a little different, so beware. Hope this helps!

Target Market(s)

Businesses - Small to Medium, Corporations, Publicly Traded Companies

Industry/Entity Type

Business

Contact Information for Business Card

Harbor Circuit IT
7180 Dorrance Avenue
Suite K
Modesto, CA 95419

Office 209.555.0137
Direct 209.555.0162
Cell 209.555.0188

Gary Stroud
Founder, CEO
www.hcxit.example
gstroud@hcxit.example

Locations Serviced: Modesto, Stockton, Pleasanton, Fresno (incorporate this on the card ONLY if there's a good place to do so).

What we specialize in: Computer, Network, Voice, Data. (IT Services)

Our Logo Colors: Black and Blue (#006699). Open to using grey or orange as well - but not required. Don't want too busy....

Logo Font: "Voralyn" (Will attach logo font). We want type style to be clean. You can show different font types including our logo font - and we are open to other font ideas.

The logo can be separated. You can use elements together or apart. Surprise us! :) We "REALLY" want the "hc" to be our identifier/our brand people recognize.

Font styles to use
Sans Serif

Colors
0355a3
3176b5
f37122
f78f20
faa54b
474747
aaaaaa
757575
000000

Requirements
Must have
• Bold, Big, Colorful, Modern/yet Fun, Clean Design, Stand Out Presence, Texture would be welcomed - but not necessary, Card design shape can include cut corners or rounded or square edges. Be creative. (HOWEVER, we don't want a square design because we have found it doesn't fit in wallets that easily).
• We do like using ZEPL printing company (Which they have particular sizing on their card templates - beware), but are open to other design templates/printing companies as well. We just want to make sure its easy to find a print company to do our work. Too unique could be costly and hard to get cards printed.
• Colors to use: Our logo Blue (#006699), with either whites, grays, black, shades of our blue, and maybe a pinch of orange if needed. Primarily, blue, white, gray or black.
Nice to have
• Texture would be cool or little different edging or shape - but nothing too costly to print. I have seen cards with 3 sharp edges and one round edge. Something like that would be cool as an option. Or a vertical card.
• I love a faded watermark look. It would be nice to see some shading of our circle logo on a few designs. The circle with "hc" in it OR.... taking just the "hc" and using it alone.
Should not have
• No square card designs. Nothing too expensive or elaborate to print. No busy fonts. Do not like Times New Roman type fonts (too old looking). Not a lot of orange (if you even choose to use some orange).

```html
<!DOCTYPE html>
<html lang="en">
<head>
<meta charset="utf-8">
<title>Harbor Circuit IT – Business Card</title>
<link href="https://fonts.googleapis.com/css2?family=Barlow:wght@400;500;600&display=swap" rel="stylesheet">
<style>
  :root {
    --stage: #2b2b2b;
    --card-top: #1a7bb4;
    --card-mid: #16689e;
    --card-bottom: #125a8c;
    --card-top-bright: #1f8fcc;
    --ink: #ffffff;
    --ink-soft: rgba(255,255,255,0.88);
    --rule: rgba(255,255,255,0.85);
  }
  * { margin: 0; padding: 0; box-sizing: border-box; }
  html, body {
    width: 1200px; height: 896px; overflow: hidden;
    background: var(--stage);
    font-family: "Barlow", "Helvetica Neue", Arial, sans-serif;
    color: var(--ink);
  }
  .canvas { position: relative; width: 1200px; height: 896px; }
  .card {
    position: absolute; top: 180px; width: 298px; height: 535px;
    overflow: hidden;
  }
  .card-front {
    left: 281px;
    border-radius: 28px 0 28px 0;
    background: linear-gradient(180deg, var(--card-top) 0%, var(--card-mid) 60%, var(--card-bottom) 100%);
  }
  .card-back {
    left: 628px;
    border-radius: 0 28px 0 28px;
    background: linear-gradient(200deg, var(--card-top-bright) 0%, var(--card-mid) 55%, var(--card-bottom) 100%);
  }
  .brand-mark {
    position: absolute; left: 105px; top: 68px;
    width: 88px; height: 88px; border-radius: 50%;
    background: var(--ink);
  }
  .brand-name {
    position: absolute; left: 0; right: 0; top: 172px;
    text-align: center; font-weight: 600; font-size: 36px;
    line-height: 1.05; letter-spacing: 0.5px; color: var(--ink);
  }
  .back-content { position: absolute; left: 39px; top: 76px; right: 20px; }
  .person-name { font-size: 29px; font-weight: 500; letter-spacing: 1px; line-height: 1; }
  .person-title { font-size: 16px; font-weight: 400; color: var(--ink-soft); margin-top: 9px; letter-spacing: 0.3px; }
  .rule { width: 147px; height: 1px; background: var(--rule); }
  .rule-top { margin-top: 25px; }
  .phones { margin: 12px 0 11px; font-size: 14px; line-height: 18px; letter-spacing: 0.6px; }
  .phones dt { float: left; width: 61px; clear: left; }
  .phones dd { margin-left: 61px; }
  .email { margin-top: 28px; font-size: 14px; letter-spacing: 0.4px; }
  .email .label { display: inline-block; width: 61px; }
  .address { margin-top: 24px; font-size: 14px; line-height: 18px; font-style: normal; letter-spacing: 0.4px; }
  .website { margin-top: 25px; font-size: 14px; letter-spacing: 0.4px; }
  .website b { font-weight: 600; }
</style>
</head>
<body>
<main class="canvas">
  <section class="card card-front" aria-label="Card front">
    <span class="brand-mark" aria-hidden="true"></span>
    <p class="brand-name">Harbor<br>Circuit</p>
  </section>

  <section class="card card-back" aria-label="Card back">
    <div class="back-content">
      <h1 class="person-name">GARY STROUD</h1>
      <p class="person-title">Founder, CEO</p>
      <div class="rule rule-top"></div>
      <dl class="phones">
        <dt>OFFICE</dt><dd>209.555.0137</dd>
        <dt>DIRECT</dt><dd>209.555.0162</dd>
        <dt>CELL</dt><dd>209.555.0188</dd>
      </dl>
      <div class="rule"></div>
      <p class="email"><span class="label">EMAIL</span>gstroud@hcxit.example</p>
      <address class="address">7180 Dorrance<br>Avenue Suite K Modesto,<br>CA 95419</address>
      <p class="website">www.<b>hcxit</b>.example</p>
    </div>
  </section>
</main>
</body>
</html>
```